Promotional Flyer for "Ventaro events" with LOGO DESIGN

I am developing my own start-up company which is organising and managing exclusive and luxury events in Vienna, London, and Venice. Elegant promotional flyer should introduce and promote my company to a broad spectrum of high level clients; both online and by regular hardcopy post. This flyer should reflect the highest level of elegance, professionalism, creativity, sophistication, and exclusivity as well as irradiating a feeling of child like joy . I want the flyer to be two sided or folded, but did not find that version. It should be including the photo from the main page of the site "www.ventaro-events.example". Text should contain the following :
Creative ideas and event concept
Unique venue selection
Complete planning and coordination
First class catering
Professional photography and video productions ---
--------------------------------------------------------------------
1.Surprise the unsurprisable
2. we materialise your innermost dreams into trend setting entertainment and unique celebration of any occasion
------------------------------------------------------------------------
You can take ideas from any photo on my website, I also add some additional photos
I am available via e-mail or phone +390000000000 /+440000000000. Thank you.

Target Market(s)

high level discreet and the discerning client with taste, well travelled already spoiled

Industry/Entity Type

Event Planning

Font styles to use
Sans Serif

Colors
ffffff
fffbf0

Requirements
Must have
• unexpected simlicity, be extremely different from all what is there on the market
Should not have
• eye catching and memorable yet not too busy

```html
<!DOCTYPE html>
<html lang="en">
<head>
<meta charset="utf-8">
<title>Ventaro events – flyer</title>
<link rel="stylesheet" href="https://fonts.googleapis.com/css2?family=Open+Sans:wght@300;400;700&display=swap">
<style>
  :root {
    --page: #e4e4e4;
    --band: #0b0a0a;
    --panel: #3b3a3a;
    --gold: #e2b13a;
    --gold-deep: #b8871f;
    --text: #f4f2ec;
    --text-soft: #d9d6cf;
  }
  * { margin: 0; padding: 0; box-sizing: border-box; }
  html, body {
    width: 924px; height: 1200px; overflow: hidden;
    background: var(--page);
    font-family: "Open Sans", Arial, sans-serif;
  }
  .flyer-side {
    position: absolute; left: 40px; width: 844px; height: 560px;
    background: var(--band);
    box-shadow: 0 6px 18px rgba(0,0,0,.35);
    overflow: hidden;
  }
  .flyer-front { top: 30px; }
  .flyer-back { top: 610px; }

  .visual-row { position: absolute; top: 0; left: 0; width: 844px; height: 395px; display: flex; }
  .photo-main { width: 580px; height: 395px;
    background: radial-gradient(ellipse at 45% 70%, #c7802c 0%, #6a3a1c 35%, #2a1a1e 65%),
                linear-gradient(#3c2250, #1a1212); background-blend-mode: screen; }
  .photo-stack { width: 264px; height: 395px; display: flex; flex-direction: column; gap: 1px; background: #000; }
  .photo-stack > div { flex: 1; }
  .photo-corks { background: linear-gradient(135deg, #d9b27a, #8a5a2c); }
  .photo-table { background: radial-gradient(circle at 50% 55%, #f08a3c, #a8451e 70%); }
  .photo-salon { background: linear-gradient(160deg, #d8b070, #7a5424); }
  .photo-ballroom { background: radial-gradient(ellipse at 50% 30%, #f3d7a0, #8a6234 75%); }
  .photo-costume { background: radial-gradient(circle at 50% 50%, #b9a1c8, #2a2570 75%); }
  .photo-masks { background: radial-gradient(circle at 50% 55%, #e8c2b2, #3a1810 75%); }

  .info-panel { width: 580px; height: 395px; background: var(--panel); padding: 30px 40px 0 58px; color: var(--text); }
  .headline { font-weight: 300; font-size: 34px; color: var(--gold); line-height: 1.1; }
  .intro { font-weight: 400; font-size: 16px; line-height: 1.35; margin-top: 6px; color: var(--text-soft); }
  .services { list-style: none; margin-top: 12px; }
  .services li { font-size: 16px; font-weight: 400; line-height: 27px; color: var(--text-soft); display: flex; align-items: center; }
  .services li::before { content: ""; width: 10px; height: 10px; border: 2px solid var(--gold); border-radius: 50%; margin-right: 10px; flex: none; }
  .contacts { margin-top: 14px; font-size: 16px; line-height: 26px; color: var(--text); }
  .contacts b { font-weight: 700; }

  .brand-band { position: absolute; left: 0; bottom: 0; width: 844px; height: 165px; }
  .bokeh { position: absolute; border-radius: 50%; background: rgba(140,120,40,.45); }
  .brand-name { position: absolute; left: 70px; top: 56px; font-size: 32px; font-weight: 400; line-height: 40px; color: var(--gold); white-space: nowrap; }
  .tagline { position: absolute; left: 345px; top: 66px; font-size: 15px; font-weight: 400; line-height: 22px; letter-spacing: 1px; color: var(--text-soft); white-space: nowrap; }
  .seal { position: absolute; right: 44px; top: -32px; width: 100px; height: 100px; border-radius: 50%;
    background: radial-gradient(circle at 40% 35%, #f2d06a, var(--gold-deep)); }
</style>
</head>
<body>

<section class="flyer-side flyer-front">
  <div class="visual-row">
    <div class="photo-main" role="img" aria-label="Ancient colonnaded ruins lit in warm gold at dusk with guests at an evening reception"></div>
    <div class="photo-stack">
      <div class="photo-corks" role="img" aria-label="Wine corks around an antique compass"></div>
      <div class="photo-table" role="img" aria-label="Candlelit table with orange flower centrepiece"></div>
      <div class="photo-salon" role="img" aria-label="Elegant gilded salon with chandelier"></div>
    </div>
  </div>
  <div class="brand-band">
    <span class="bokeh" style="left:22px;top:18px;width:26px;height:26px"></span>
    <span class="bokeh" style="left:36px;top:90px;width:20px;height:20px"></span>
    <span class="bokeh" style="left:360px;top:4px;width:10px;height:10px"></span>
    <div class="brand-name">Ventaro events</div>
    <div class="tagline">EXCLUSIVE / EXTRAORDINARY / EXOTIC</div>
    <div class="seal" role="img" aria-label="Gold seal"></div>
  </div>
</section>

<section class="flyer-side flyer-back">
  <div class="visual-row">
    <div class="info-panel">
      <h1 class="headline">Surprise the unsurprisable</h1>
      <p class="intro">We materialise your innermost dreams into trend setting entertainment and unique celebration of any occasion.</p>
      <ul class="services">
        <li>Creative ideas and event concept</li>
        <li>Unique venue selection</li>
        <li>Complete planning and coordination</li>
        <li>First class catering</li>
        <li>Professional photography and video productions</li>
      </ul>
      <div class="contacts">
        <div><b>Locations:</b> London / Venice / Moscow / New York</div>
        <div><b>Call now</b> +390000000000 / +440000000000</div>
        <div><b>Email:</b> marketing@ventaro-events.example</div>
        <div><b>Website:</b> www.ventaro-events.example</div>
      </div>
    </div>
    <div class="photo-stack">
      <div class="photo-ballroom" role="img" aria-label="Crowded baroque ballroom under crystal chandeliers"></div>
      <div class="photo-costume" role="img" aria-label="Winged stage performer in purple light"></div>
      <div class="photo-masks" role="img" aria-label="Performers in Venetian carnival gowns"></div>
    </div>
  </div>
  <div class="brand-band">
    <span class="bokeh" style="left:18px;top:8px;width:26px;height:26px"></span>
    <span class="bokeh" style="left:30px;top:84px;width:20px;height:20px"></span>
    <span class="bokeh" style="left:350px;top:26px;width:10px;height:10px"></span>
    <div class="brand-name">Ventaro events</div>
    <div class="tagline">EXCLUSIVE / EXTRAORDINARY / EXOTIC</div>
  </div>
</section>

</body>
</html>
```